Riverbend Haven Home Care-Flyer for Patients

Our Home Health Care Agency, Riverbend Haven Home Care, is seeking a flyer to advertise our services. We would like our flyer to convey professionalism, classiness and sophistication. We want our agency to come across as one that is well-established and recognized as being first-rate within the field.

We also want to appear original; we want to stand out.

Our theme colors, blue and green, from our logo should be incorporated into the flyer's design (refer below).

The top of the page should say (in a clear, bold font)-Seeking Care for your Loved One?

Our Logo, followed by our slogan, "Let Your Neighbors Look After You", should be in the center. (This should make it appear as if our agency is the obvious solution to the consumer's quest in finding suitable care for their family member). This should be in a big font.
Below that, our agency's services should be listed in a very noticeable font...yet smaller than what's written above that.
The text should read:
Our Services Include:
*Experienced Certified Home Health Aides/ Live In Home Health Aides/Companions
*Nursing Services
*Alzheimer’s and Dementia Care
*Respite Care
*Postoperative Care
*Post Rehabilitation Care
*Running Errands
*Light Housekeeping
*Assistance with Bathing, Feeding and Grooming
*Meal Preparation
*Laundry and Linen Washing
*Mail and Bill Organization
*Medication Management
*Accompanying to Doctor’s Appointments
*And much more!
Below that, in a smaller, yet noticeable font:
As seasoned professionals, we know how to help our clients navigate and fulfill their various health care needs. Your Community is here to help you get the care that you deserve.
Call Riverbend Haven Home Care today to learn more about our first-rate services!
Below that, in a larger font, our phone number, website, our e-mail address.
*Out contact information will be provided to the project’s winner*.

*Pictures of Caregivers helping elderly patient should be included in the advertisement as well. *

We provided advertisements of other Home Health Care Agencies attached below to use as a reference. Once again, while we are aiming for a similar idea; however, our goal is to stand out as the community's premiere home health care agency, the one that they want to choose. We want to be original as well!

Size: Standard Computer Paper Size. 8.5” x 11”.

Feel free to utilize your creative, designer flair!
We look forward to seeing the results!
Good luck!

Industry/Entity Type

Home Health Care

Font styles to use
Sans Serif

Requirements
Must have
• Refer above.
Nice to have
• Refer to attachment below to see how other home health care agencies advertise. While we are aiming for a similar idea, we would like to incorporate our logo, slogan and colors to make this flyer more unique and stand out. We would like to appear original.

```html
<!DOCTYPE html>
<html lang="en">
<head>
<meta charset="utf-8">
<title>Riverbend Haven Home Care – Flyer</title>
<link href="https://fonts.googleapis.com/css2?family=Montserrat:wght@600;700;800;900&family=Open+Sans:wght@400;600;700&display=swap" rel="stylesheet">
<style>
  :root{
    --blue:#17479e;
    --blue-deep:#123a86;
    --green:#7ac143;
    --green-dark:#5fa52c;
    --ink:#1d2a44;
    --white:#ffffff;
    --page:#f2f2f2;
  }
  *{box-sizing:border-box;margin:0;padding:0}
  html,body{width:848px;height:1200px;overflow:hidden;background:var(--page)}
  .flyer{position:relative;width:848px;height:1200px;background:var(--white);overflow:hidden;font-family:"Open Sans",Arial,sans-serif;color:var(--ink)}

  .hero-photo{position:absolute;left:0;top:150px;width:848px;height:620px;
    background:
      linear-gradient(90deg,rgba(255,255,255,.92) 0%,rgba(255,255,255,.55) 28%,rgba(255,255,255,0) 50%),
      linear-gradient(180deg,rgba(255,255,255,1) 0%,rgba(255,255,255,0) 14%),
      radial-gradient(ellipse at 62% 40%,#e9d6c6 0%,#d9c7b3 22%,#c9c3ba 40%,#dfe3e0 62%,#eef1ee 100%);}
  .hero-edge{position:absolute;right:0;top:150px;width:90px;height:620px;background:linear-gradient(90deg,rgba(120,120,120,0),rgba(90,90,90,.35))}

  .swoosh{position:absolute;left:0;top:0;width:848px;height:1200px}

  .brand{position:absolute;left:58px;top:48px;width:210px;text-align:center}
  .brand-mark{width:62px;height:62px;border-radius:50%;background:var(--blue);margin:0 auto 10px}
  .brand-name{font-family:"Montserrat",Arial,sans-serif;font-weight:700;font-size:15px;line-height:1.2;color:var(--blue);text-transform:uppercase;letter-spacing:.3px}

  .headline{position:absolute;left:292px;top:44px}
  .headline-lead{font-family:"Montserrat",Arial,sans-serif;font-weight:800;font-size:34px;color:var(--blue);letter-spacing:.5px;line-height:1}
  .headline-main{font-family:"Montserrat",Arial,sans-serif;font-weight:900;font-size:70px;color:var(--green);line-height:1;margin-top:6px;letter-spacing:1px}

  .slogan{position:absolute;left:0;width:848px;top:742px;text-align:center;font-family:"Montserrat",Arial,sans-serif;font-weight:800;font-size:37px;color:var(--blue)}
  .slogan .accent{color:var(--green)}

  .services-tab{position:absolute;left:326px;top:806px;width:196px;height:50px;background:var(--blue);border-radius:28px 28px 0 0;color:var(--white);font-family:"Montserrat",Arial,sans-serif;font-weight:700;font-size:27px;text-align:center;line-height:54px}
  .services-rule{position:absolute;left:55px;right:55px;top:855px;height:3px;background:var(--blue)}

  .services{position:absolute;top:872px;list-style:none;font-size:13px;font-weight:600;line-height:1.2;color:var(--ink)}
  .services li{position:relative;padding-left:24px;margin-bottom:9px}
  .services li::before{content:"";position:absolute;left:2px;top:1px;width:12px;height:12px;border:1.5px solid var(--blue);border-radius:50%}
  .services li::after{content:"";position:absolute;left:6px;top:3px;width:3px;height:6px;border:solid var(--blue);border-width:0 1.6px 1.6px 0;transform:rotate(45deg)}
  .col-one{left:52px;width:245px}
  .col-two{left:316px;width:240px}
  .col-three{left:578px;width:240px}

  .mission{position:absolute;left:55px;right:55px;top:1034px;height:52px;background:var(--green);border-radius:12px;color:var(--white);font-size:13.5px;line-height:1.15;text-align:center;padding:11px 30px}

  .call{position:absolute;left:0;width:848px;top:1104px;text-align:center;font-family:"Montserrat",Arial,sans-serif;font-weight:700;font-size:22px;color:var(--blue)}

  .contact{position:absolute;left:55px;right:55px;top:1146px;display:flex;justify-content:space-between;align-items:center}
  .contact-item{display:flex;align-items:center;gap:7px;font-weight:700;font-size:14px;color:var(--blue-deep)}
  .contact-phone{font-family:"Montserrat",Arial,sans-serif;font-size:24px;color:var(--blue)}
  .contact-item svg{flex:none}
</style>
</head>
<body>
<main class="flyer">

  <div class="hero-photo" role="img" aria-label="Photo of a smiling young caregiver with her arm around an elderly woman in a bright room"></div>
  <div class="hero-edge"></div>

  <svg class="swoosh" viewBox="0 0 848 1200" aria-hidden="false">
    <defs>
      <linearGradient id="photoOne" x1="0" y1="0" x2="1" y2="1">
        <stop offset="0" stop-color="#8fae6a"/><stop offset=".5" stop-color="#cfd9c4"/><stop offset="1" stop-color="#e8cdb8"/>
      </linearGradient>
      <linearGradient id="photoTwo" x1="0" y1="0" x2="1" y2="1">
        <stop offset="0" stop-color="#d8dde2"/><stop offset=".5" stop-color="#9fb1c3"/><stop offset="1" stop-color="#3d5f8c"/>
      </linearGradient>
      <linearGradient id="photoThree" x1="0" y1="0" x2="1" y2="1">
        <stop offset="0" stop-color="#c9d6dc"/><stop offset=".5" stop-color="#4aa3b6"/><stop offset="1" stop-color="#2a2a2e"/>
      </linearGradient>
    </defs>

    <!-- white ground below the band -->
    <path d="M0 770 C 60 712, 120 690, 200 686 L 660 664 C 750 660, 810 640, 848 612 L 848 1200 L 0 1200 Z" fill="#ffffff"/>
    <!-- green sweep band -->
    <path d="M0 780 C 50 700, 110 650, 190 640 L 660 600 C 760 592, 820 575, 848 555 L 848 612 C 810 642, 750 662, 660 666 L 200 688 C 120 694, 60 716, 0 780 Z" fill="var(--green)"/>

    <!-- circle one -->
    <g>
      <circle cx="172" cy="608" r="104" fill="var(--green)"/>
      <circle cx="178" cy="604" r="92" fill="var(--white)"/>
      <circle cx="180" cy="604" r="88" fill="var(--blue)"/>
      <circle cx="183" cy="602" r="82" fill="url(#photoOne)" role="img" aria-label="Photo of a caregiver in scrubs walking arm in arm with an elderly woman in a garden"/>
    </g>
    <!-- circle two -->
    <g>
      <circle cx="412" cy="580" r="98" fill="var(--green)"/>
      <circle cx="418" cy="576" r="86" fill="var(--white)"/>
      <circle cx="420" cy="576" r="82" fill="var(--blue)"/>
      <circle cx="423" cy="574" r="76" fill="url(#photoTwo)" role="img" aria-label="Photo of an elderly man in a wheelchair giving a high five to a nurse"/>
    </g>
    <!-- circle three -->
    <g>
      <circle cx="660" cy="622" r="106" fill="var(--green)"/>
      <circle cx="666" cy="618" r="94" fill="var(--white)"/>
      <circle cx="668" cy="618" r="90" fill="var(--blue)"/>
      <circle cx="671" cy="616" r="84" fill="url(#photoThree)" role="img" aria-label="Photo of a caregiver helping an older woman with her medication"/>
    </g>
  </svg>

  <header class="brand">
    <div class="brand-mark"></div>
    <div class="brand-name">Riverbend Haven Home Care</div>
  </header>

  <h1 class="headline">
    <span class="headline-lead">Seeking Care For Your</span><br>
    <span class="headline-main">LOVED ONE?</span>
  </h1>

  <h2 class="slogan">Let Your Neighbors <span class="accent">Look After You</span></h2>

  <div class="services-tab">Our Services</div>
  <div class="services-rule"></div>

  <ul class="services col-one">
    <li>Experienced Certified Home Health Aides Live In Home Health Aides/Companions</li>
    <li>Nursing Services</li>
    <li>Alzheimer’s and Dementia Care</li>
    <li>Respite Care</li>
    <li>Postoperative Care</li>
  </ul>
  <ul class="services col-two">
    <li>Post Rehabilitation Care</li>
    <li>Running Errands</li>
    <li>Light Housekeeping</li>
    <li>Assistance with Bathing, Feeding and Grooming</li>
    <li>Meal Preparation</li>
  </ul>
  <ul class="services col-three">
    <li>Laundry and Linen Washing</li>
    <li>Mail and Bill Organization</li>
    <li>Medication Management</li>
    <li>Accompanying to Doctor’s Appointments</li>
  </ul>

  <p class="mission">As seasoned professionals, we know how to help our clients navigate and fulfill their various health care needs. Your Community is here to help you get the care that you deserve.</p>

  <p class="call">Call Today to Hear About out First-rate services!</p>

  <footer class="contact">
    <span class="contact-item contact-phone">
      <svg width="16" height="18" viewBox="0 0 24 24"><path d="M6.6 10.8c1.4 2.8 3.8 5.1 6.6 6.6l2.2-2.2c.3-.3.7-.4 1-.2 1.1.4 2.3.6 3.6.6.6 0 1 .4 1 1V20c0 .6-.4 1-1 1C10.6 21 3 13.4 3 4c0-.6.4-1 1-1h3.5c.6 0 1 .4 1 1 0 1.3.2 2.5.6 3.6.1.3 0 .7-.2 1L6.6 10.8z" fill="var(--green)"/></svg>
      1800-555-0147
    </span>
    <span class="contact-item">
      <svg width="13" height="10" viewBox="0 0 26 20"><rect width="26" height="20" rx="2" fill="var(--green)"/><path d="M1 2 L13 11 L25 2" stroke="#fff" stroke-width="2.4" fill="none"/></svg>
      www.riverbendhaven.com
    </span>
    <span class="contact-item">
      <svg width="12" height="12" viewBox="0 0 24 24"><circle cx="12" cy="12" r="11" fill="var(--green)"/><path d="M1 12h22M12 1c4 3.5 4 18.5 0 22M12 1c-4 3.5-4 18.5 0 22" stroke="#fff" stroke-width="1.6" fill="none"/></svg>
      hello@riverbendhaven.com
    </span>
  </footer>

</main>
</body>
</html>
```